Medical Clinic Website Makeover

Our website needs a make over. We would like something appealing, modern, captivating and aesthetically pleasing for our medical practice.
The website must be informative whilst flowing with ease and also entice patients to explore the website.

It is essential that the website is compatible across all devices and user friendly, especially when it comes to updating details within the website etc.

Our current page is http://www.brightpathclinicwest.com.au

Given the multiple locations of which we currently consult and operate from, our contact page should include a clear map outlining each clinic location.
- 48 Thornbury Street Echuca VIC 3550
- 293 Kestrel Street Bendigo Vic 3550
- Suite 5/417 Juniper Avenue Mildura VIC 3500
- Level 7, 612 Harwood Street Melbourne Vic 3000
- 284 Marlow Road, Cnr Oakvale Road Bundoora VIC 3083

The pages to be included should be as follows:
Home
About
Our Clinic
Booking
ENT Conditions
Facial Plastics
Contact
Updates

Target Market(s)

Adults, Families

Coding

Coded - Design and coding required

Number of Pages Required

5+ page

Requirements
Must have
• Modern
Captivating
Aesthetically pleasing

Online booking page
Nice to have
• It would be great to have the option for instant chat for patients that have enquiries

A page for patients to make payments online would be amazing. Here is an example of another website that does this: https://vantorhq.com.au/payment ( this MUST be secure)

```html
<!DOCTYPE html>
<html lang="en">
<head>
<meta charset="utf-8">
<title>Brightpath ENT West</title>
<link href="https://fonts.googleapis.com/css2?family=Poppins:wght@300;400;500;600&display=swap" rel="stylesheet">
<style>
:root{
  --blue:#2c3c9c;
  --blue-deep:#23348c;
  --purple:#8e3a9d;
  --sky:#2ea3dc;
  --bg:#f4f6fb;
  --ink:#1f1f2a;
  --muted:#6b6f7b;
  --footer:#1f2533;
  --footer-low:#1a1f2b;
}
*{margin:0;padding:0;box-sizing:border-box}
html,body{width:1200px;height:4258px;overflow:hidden}
body{position:relative;background:var(--bg);font-family:'Poppins',sans-serif;color:var(--ink)}
.abs{position:absolute}
.center{text-align:center;left:0;width:1200px}
/* header */
.hero-photo{left:0;top:0;width:1200px;height:727px}
.top-links{top:24px;right:50px;display:flex;gap:46px;align-items:center;color:var(--blue);font-size:19px;font-weight:500}
.top-links .call{display:flex;align-items:center;gap:14px;font-size:21px}
.brand{left:52px;top:62px;display:flex;align-items:center;gap:12px}
.brand .dot{width:50px;height:50px;border-radius:50%;background:var(--blue)}
.brand span{font-size:32px;font-weight:400;color:var(--blue);letter-spacing:-.5px}
.nav{left:440px;top:69px;width:593px;height:67px;background:#fff;display:flex;align-items:center;justify-content:space-around;font-size:17px;font-weight:500}
.booking{left:1033px;top:69px;width:167px;height:67px;background:var(--blue);color:#fff;font-size:17px;font-weight:500;display:flex;align-items:center;justify-content:center}
.hero-caption{left:372px;top:413px;width:454px;height:103px;background:rgba(40,40,50,.55);color:#fff;text-align:center;font-size:20px;line-height:30px;padding-top:20px}
.btn-appt{left:489px;top:562px;width:222px;height:43px;border-radius:22px;background:var(--blue);color:#fff;font-size:17px;display:flex;align-items:center;justify-content:center}
/* section heads */
.eyebrow{font-size:14px;color:var(--muted);letter-spacing:.5px}
.title{font-size:43px;font-weight:300}
.rule{left:580px;width:40px;height:3px;background:var(--purple)}
/* service cards */
.map-dots{left:470px;top:900px;width:610px;height:280px;border-radius:50%;background:radial-gradient(ellipse,rgba(200,205,220,.45),rgba(244,246,251,0) 70%)}
.card-bg{left:119px;top:937px;width:326px;height:306px;background:#fff;box-shadow:0 12px 30px rgba(30,40,80,.1)}
.svc{width:260px;text-align:center}
.svc h3{font-size:17px;font-weight:500;margin-top:38px}
.svc p{font-size:12px;color:var(--muted);line-height:23px;margin-top:20px}
/* team */
.team{top:1496px;height:484px;width:400px}
.team.t1{left:0;background:linear-gradient(160deg,#3a4ea8,#2a3a94)}
.team.t2{left:400px;background:linear-gradient(180deg,#a9b2c6,#3c4152 60%,#23262f)}
.team.t3{left:800px;background:linear-gradient(180deg,#c4c8d2,#4a3f3a 55%,#1f1d22)}
.team-txt{text-align:center;color:#fff;width:400px}
.team-txt h4{font-size:19px;font-weight:500}
.team-txt p{font-size:15px;line-height:23px;margin-top:12px;font-weight:300}
.bio{left:132px;top:1889px;width:136px;height:38px;border-radius:19px;background:#fff;color:var(--ink);font-size:15px;display:flex;align-items:center;justify-content:center}
/* appointment */
.lead{font-size:16px;line-height:30px}
.check-item{font-size:16px;line-height:27px;width:270px}
.conn{height:2px;background:var(--sky)}
/* contact band */
.band{left:0;top:2691px;width:1200px;height:231px;background:var(--blue);overflow:hidden}
.band-label{left:164px;top:2754px;color:#fff;font-size:22px;font-weight:300}
.band-title{left:164px;top:2795px;color:#fff;font-size:38px;font-weight:300}
.band-btn{left:785px;top:2787px;width:155px;height:45px;border-radius:23px;background:#fff;color:var(--blue);font-size:16px;display:flex;align-items:center;justify-content:center}
/* form */
.field{top:3179px;width:244px;height:39px;border:1px solid #d9dce4;background:#fff;font-size:14px;color:#9a9eaa;padding:9px 18px}
.submit{left:536px;top:3256px;width:129px;height:45px;background:var(--blue);color:#fff;font-size:16px;font-weight:500;display:flex;align-items:center;justify-content:center}
/* testimonial */
.quote{left:511px;top:3588px;width:440px;font-size:16px;line-height:33px;color:var(--muted)}
.qname{left:511px;top:3712px;font-size:15px;color:var(--sky);font-weight:500}
/* footer */
.footer{left:0;top:3843px;width:1200px;height:323px;background:var(--footer)}
.footer-low{left:0;top:4166px;width:1200px;height:92px;background:var(--footer-low)}
.fh{top:3921px;color:#fff;font-size:15px;font-weight:600}
.flist{top:3956px;color:#b7bccb;font-size:13px;line-height:28px;list-style:none}
.fc{color:#b7bccb;font-size:13px;line-height:23px;display:flex;gap:12px;align-items:flex-start}
.news{left:752px;top:4026px;width:331px;height:35px;border-radius:18px;background:#fff;overflow:hidden;display:flex;font-size:13px}
.news span{flex:1;padding:8px 22px;color:#9a9eaa}
.news b{width:119px;background:var(--sky);color:#fff;font-weight:500;display:flex;align-items:center;justify-content:center}
.copy{left:117px;top:4193px;color:#b7bccb;font-size:13px}
.foot-brand{left:520px;top:4183px;display:flex;gap:10px;align-items:center;color:#fff;font-size:22px}
.foot-brand i{width:26px;height:26px;border-radius:50%;background:var(--blue);display:block}
.socials{left:955px;top:4198px;display:flex;gap:14px}
.socials i{width:12px;height:12px;border-radius:50%;background:#b7bccb;display:block}
</style>
</head>
<body>

<!-- hero -->
<svg class="abs hero-photo" viewBox="0 0 1200 727" role="img" aria-label="Photo of the three clinic surgeons standing together in a bright clinic">
  <defs>
    <linearGradient id="heroG" x1="0" y1="0" x2="0" y2="1">
      <stop offset="0" stop-color="#f3ede6"/>
      <stop offset=".45" stop-color="#c9b7a6"/>
      <stop offset="1" stop-color="#2a2b33"/>
    </linearGradient>
  </defs>
  <polygon points="0,0 1200,0 1200,620 600,727 0,620" fill="url(#heroG)"/>
  <polyline points="0,620 600,727 1200,620" fill="none" stroke="#c7cde0" stroke-width="3"/>
</svg>

<div class="abs top-links">
  <span>Contact Us</span>
  <span class="call">Call
    <svg width="34" height="34" viewBox="0 0 24 24" fill="none" stroke="#2c3c9c" stroke-width="1.4"><path d="M5 3h4l2 5-2.5 1.5a11 11 0 0 0 6 6L16 13l5 2v4a2 2 0 0 1-2 2A16 16 0 0 1 3 5a2 2 0 0 1 2-2z"/></svg>
    03 5550 1180</span>
</div>

<div class="abs brand"><i class="dot"></i><span>Brightpath ENT</span></div>

<nav class="abs nav"><span>About</span><span>Our Clinic</span><span>ENT Conditions</span><span>Facial Plastics</span></nav>
<div class="abs booking">Booking</div>

<div class="abs hero-caption">BRIGHTPATH ENT WEST<br>EAR NOSE &amp; THROAT SURGEONS</div>
<div class="abs btn-appt">Get Appointment</div>

<!-- services -->
<div class="abs center eyebrow" style="top:793px">WHAT WE DO</div>
<div class="abs center title" style="top:820px">Our Services</div>
<div class="abs rule" style="top:886px"></div>

<div class="abs map-dots" role="img" aria-label="Faint dotted world map"></div>
<div class="abs card-bg"></div>

<div class="abs svc" style="left:153px;top:988px">
  <svg width="56" height="70" viewBox="0 0 56 70" fill="none" stroke="#2c3c9c" stroke-width="2.5"><path d="M14 58c0-14-6-18-6-32a20 20 0 0 1 40 0c0 12-10 14-10 24a8 8 0 0 1-16 0"/><path d="M22 26a6 6 0 0 1 12 0c0 6-6 6-6 12" stroke="#8e3a9d"/></svg>
  <h3 style="margin-top:26px">Ear Conditions</h3>
  <p>Glue ear is the commonest cause of hearing loss in children. It refers to thick fluid</p>
</div>
<div class="abs svc" style="left:525px;top:988px">
  <svg width="56" height="70" viewBox="0 0 56 70" fill="none" stroke="#2c3c9c" stroke-width="2.5"><path d="M28 4c4 14 12 26 12 40a12 12 0 0 1-24 0c0-14 8-26 12-40z"/><circle cx="22" cy="48" r="3" stroke="#8e3a9d"/><circle cx="34" cy="48" r="3" stroke="#8e3a9d"/></svg>
  <h3 style="margin-top:26px">Nasal Conditions</h3>
  <p>The nose is responsible for 25% of breathing function and everyone knows what a blocked nose feels like.</p>
</div>
<div class="abs svc" style="left:834px;top:988px">
  <svg width="70" height="70" viewBox="0 0 70 70" fill="none" stroke="#2c3c9c" stroke-width="2.5"><path d="M30 64V44c-6-2-8-8-6-14 2-10 10-18 22-18s20 8 20 20c0 8-4 12-8 16v16"/><path d="M4 30h14M6 38h12M4 46h14" stroke="#8e3a9d"/></svg>
  <h3 style="margin-top:26px">Throat Conditions</h3>
  <p>Mr Hale has undertaken cancer surgery in the Head and Neck for more than 15 years</p>
</div>

<div class="abs center eyebrow" style="top:1348px">WHAT WE DO</div>
<div class="abs center title" style="top:1375px">Our Services</div>
<div class="abs rule" style="top:1441px"></div>

<!-- team -->
<div class="abs team t1" role="img" aria-label="Portrait of Dr Marcus Hale with a blue overlay"></div>
<div class="abs team t2" role="img" aria-label="Portrait of the clinic anaesthetist"></div>
<div class="abs team t3" role="img" aria-label="Portrait of the personal assistant"></div>

<div class="abs team-txt" style="left:0;top:1772px"><h4>Dr Marcus Hale</h4><p>ENT, Head, Neck,<br>Facial Plastic Surgeon</p></div>
<div class="abs bio">View Bio</div>
<div class="abs team-txt" style="left:400px;top:1795px"><h4>Dr Marcus Hale</h4><p>Anaesthetist - Brightpath<br>Anaesthetic Services</p></div>
<div class="abs team-txt" style="left:800px;top:1795px"><h4>Annika Lowell</h4><p>Personal Assistant to<br>Dr Marcus Hale</p></div>

<!-- first appointment -->
<div class="abs center title" style="top:2070px">Your First Appointment</div>
<div class="abs center lead" style="top:2135px">We want your experience with Brightpath ENT West to be a good one. To make things easier,<br>please make sure you have the following with you.</div>

<svg class="abs" style="left:430px;top:2273px" width="340" height="260" viewBox="0 0 340 260">
  <circle cx="170" cy="130" r="127" fill="#e1ecf7"/>
  <circle cx="170" cy="130" r="93" fill="#cfe2f3"/>
  <circle cx="170" cy="130" r="28" fill="#2c3c9c"/>
</svg>
<div class="abs conn" style="left:392px;top:2331px;width:91px"></div>
<div class="abs conn" style="left:383px;top:2477px;width:91px"></div>
<div class="abs conn" style="left:638px;top:2331px;width:91px"></div>
<div class="abs conn" style="left:643px;top:2477px;width:92px"></div>

<svg class="abs" style="left:180px;top:2268px" width="36" height="36" viewBox="0 0 36 36" fill="none" stroke="#1f1f2a" stroke-width="2.4"><path d="M32 16v2a14 14 0 1 1-8-13"/><path d="M12 17l6 6 14-16"/></svg>
<div class="abs check-item" style="left:177px;top:2310px">Referral letter<br>from your GP</div>
<svg class="abs" style="left:180px;top:2425px" width="36" height="36" viewBox="0 0 36 36" fill="none" stroke="#1f1f2a" stroke-width="2.4"><path d="M32 16v2a14 14 0 1 1-8-13"/><path d="M12 17l6 6 14-16"/></svg>
<div class="abs check-item" style="left:177px;top:2467px">Medicare Card or private<br>insurance details</div>
<svg class="abs" style="left:770px;top:2268px" width="36" height="36" viewBox="0 0 36 36" fill="none" stroke="#1f1f2a" stroke-width="2.4"><path d="M32 16v2a14 14 0 1 1-8-13"/><path d="M12 17l6 6 14-16"/></svg>
<div class="abs check-item" style="left:766px;top:2310px;width:290px">Physical copies of any imaging<br>(X-ray etc) or current tests</div>
<svg class="abs" style="left:770px;top:2425px" width="36" height="36" viewBox="0 0 36 36" fill="none" stroke="#1f1f2a" stroke-width="2.4"><path d="M32 16v2a14 14 0 1 1-8-13"/><path d="M12 17l6 6 14-16"/></svg>
<div class="abs check-item" style="left:769px;top:2467px;width:290px">Any other relevant doctors letters,<br>results etc, you may have.</div>

<!-- contact band -->
<div class="abs band">
  <svg width="1200" height="231" viewBox="0 0 1200 231">
    <polygon points="0,60 60,0 120,0 110,110 0,220" fill="rgba(255,255,255,.06)"/>
    <circle cx="1140" cy="100" r="110" fill="none" stroke="rgba(255,255,255,.08)" stroke-width="40"/>
  </svg>
</div>
<div class="abs band-label">Contact us</div>
<div class="abs band-title">Following a consultation</div>
<div class="abs band-btn">Contact Us</div>

<!-- enquiry form -->
<div class="abs center" style="top:3008px;font-size:31px;font-weight:300">We are always ahead</div>
<div class="abs center" style="top:3050px;font-size:31px;font-weight:600">Professional Solutions for You</div>
<div class="abs center" style="top:3112px;font-size:19px;font-weight:300">I would like to discuss</div>
<div class="abs field" style="left:216px">Name</div>
<div class="abs field" style="left:478px">Email</div>
<div class="abs field" style="left:739px">Phone</div>
<div class="abs submit">Submit</div>

<!-- testimonials -->
<svg class="abs" style="left:0;top:3350px" width="1200" height="493" viewBox="0 0 1200 493">
  <path d="M0,200 C250,80 420,120 620,150 C820,180 980,60 1200,80 L1200,493 L0,493 Z" fill="#fff"/>
</svg>
<div class="abs center" style="top:3462px;font-size:14px">Our Customer Says</div>
<div class="abs center" style="top:3488px;font-size:31px;font-weight:600">Testimonials</div>
<div class="abs" style="left:570px;top:3540px;width:60px;height:3px;background:linear-gradient(90deg,#f2a23a,#2ea3dc)"></div>

<svg class="abs" style="left:318px;top:3570px" width="160" height="140" viewBox="0 0 160 140">
  <circle cx="85" cy="70" r="66" fill="#e9eef2"/>
  <circle cx="79" cy="70" r="61" fill="#b9a79a" role="img" aria-label="Customer portrait"/>
  <circle cx="34" cy="70" r="16" fill="#f2a23a"/>
  <text x="34" y="76" text-anchor="middle" font-family="Poppins,sans-serif" font-size="16" fill="#fff">“</text>
</svg>
<div class="abs quote">This is due to their excellent service, competitive pricing and customer support. It's throughly refresing to get such a personal touch.</div>
<div class="abs qname">Renata Cole</div>
<svg class="abs" style="left:890px;top:3750px" width="64" height="20" viewBox="0 0 64 20" fill="none" stroke-width="1.8"><path d="M26 10H3M9 4L3 10l6 6" stroke="#2c3c9c"/><path d="M36 10h23M53 4l6 6-6 6" stroke="#9aa0ad"/></svg>

<!-- footer -->
<div class="abs footer"></div>
<div class="abs footer-low"></div>

<div class="abs fh" style="left:117px">Contact Us</div>
<div class="abs fc" style="left:117px;top:3962px">
  <svg width="14" height="18" viewBox="0 0 14 18" fill="none" stroke="#b7bccb" stroke-width="1.4"><path d="M7 17s6-6 6-10A6 6 0 0 0 1 7c0 4 6 10 6 10z"/><circle cx="7" cy="7" r="2"/></svg>
  <span>72 Ridley Lane #4B<br>Dallas 75201 TX</span>
</div>
<div class="abs fc" style="left:117px;top:4022px;font-size:14px;color:#fff">
  <svg width="18" height="18" viewBox="0 0 24 24" fill="none" stroke="#fff" stroke-width="1.8"><path d="M5 3h4l2 5-2.5 1.5a11 11 0 0 0 6 6L16 13l5 2v4a2 2 0 0 1-2 2A16 16 0 0 1 3 5a2 2 0 0 1 2-2z"/></svg>
  <span>(123) 555 0147</span>
</div>
<div class="abs fc" style="left:117px;top:4062px">
  <svg width="16" height="14" viewBox="0 0 16 14" fill="none" stroke="#b7bccb" stroke-width="1.3"><rect x="1" y="2" width="14" height="10"/><path d="M1 2l7 6 7-6"/></svg>
  <span>hello@brightpathent.com</span>
</div>

<div class="abs fh" style="left:410px">Quick Links</div>
<ul class="abs flist" style="left:410px"><li>Home</li><li>Oor Clinic</li><li>ENT Conditions</li><li>Facial Plastics</li><li>Bookin</li></ul>
<div class="abs fh" style="left:560px">Quick Links</div>
<ul class="abs flist" style="left:560px"><li>Support</li><li>Testimonials</li><li>Sitemap</li><li>Career</li><li>Contact Us</li></ul>
<div class="abs fh" style="left:760px">WRITE TO US</div>
<div class="abs" style="left:760px;top:3956px;color:#b7bccb;font-size:12px;line-height:24px">Provide your email below to<br>subscribe to our newsletter</div>
<div class="abs news"><span>Email address</span><b>Subscribe</b></div>

<div class="abs copy">Copyright 2020 Brightpathent.com</div>
<div class="abs foot-brand"><i></i>Brightpath ENT</div>
<div class="abs socials"><i></i><i></i><i></i><i></i><i></i></div>

</body>
</html>
```